Redesign digital storytelling app interface for picking topics and recording/listening to audio

We are building an app for users to tell stories to their friends and family in response to prompts. Our current interface is very basic, and we want to have it redesigned in order to make it more visually appealing and feel more like a comfortable conversation. We also need one screen created from scratch to match the existing screens.
In this app, the user picks a story topic from a list a friend has sent to them and then makes an audio recording in response to that topic. The other user receives the recording and listens to it, then responds to the story.
Attached are images of the screens we want to have redesigned.
1. Topic Selection Screen - screen showing the three prompts that the user will pick from before recording their story.
2. Story Recording Screen - screen that the user sees while recording their story.
3. Playback Screen - screen that the user sees while listening to the story.
4. Respond to Story Screen - screen that the user sees after listening to the story on the playback screen. This screen should have buttons for the user to communicate with the person who sent them the story, including: a quick record button where the user can send a voice message responding to the story, a phone call button, a text button, a velnorix button, and a drumo button. It should also have a button to return to the main menu.
I've also attached a graphic showing what we are currently using for a logo and color scheme. This does not need to be followed exactly.
As an added bonus, please give an example of how to manage these screens when the stories are not one-on-one, but in a group of four people.
The mood of this product should be comfortable, personal, and conversational. We want people to feel like they're chatting with an old friend. The design itself can be anything at all, so go wild!
Digital

```html
<!DOCTYPE html>
<html lang="en">
<head>
<meta charset="utf-8">
<title>Tell a Story – Pick a Topic</title>
<link rel="stylesheet" href="https://fonts.googleapis.com/css2?family=Open+Sans:wght@400;700&family=Ubuntu:wght@400;500&family=Arimo:wght@400;700&display=swap">
<style>
  :root {
    --stage: #4b4b48;
    --screen: #ffffff;
    --status-bar: #000000;
    --brand-green: #5aa32d;
    --brand-green-dark: #4c8f25;
    --ink: #222222;
    --muted: #c4c4c4;
    --card: #ececec;
    --card-shadow: rgba(0, 0, 0, 0.22);
    --alert: #d6232a;
    --avatar-a: #8a8f96;
    --avatar-b: #3d3a38;
  }
  * { box-sizing: border-box; margin: 0; padding: 0; }
  html, body {
    width: 960px; height: 1200px; overflow: hidden;
    background: var(--stage);
  }
  .app-screen {
    position: absolute; left: 144px; top: 0;
    width: 672px; height: 1200px;
    background: var(--screen);
    font-family: "Ubuntu", sans-serif;
    color: var(--ink);
  }
  .status-bar {
    height: 53px; background: var(--status-bar); color: #fff;
    font-family: "Arimo", sans-serif; font-size: 25px;
    display: flex; align-items: center; justify-content: space-between;
    padding: 0 14px 0 12px; position: relative;
  }
  .status-bar .clock {
    position: absolute; left: 0; right: 0; text-align: center; font-weight: 700;
  }
  .status-right { display: flex; align-items: center; gap: 6px; position: relative; }
  .app-bar {
    height: 65px; background: var(--brand-green);
    border-bottom: 2px solid var(--brand-green-dark);
    display: flex; align-items: center; justify-content: space-between;
    padding: 0 14px 0 10px; position: relative; color: #fff;
  }
  .app-bar .title {
    position: absolute; left: 0; right: 0; text-align: center;
    font-family: "Open Sans", sans-serif; font-weight: 700; font-size: 25px;
    pointer-events: none;
  }
  .app-bar-actions { display: flex; align-items: center; gap: 10px; }
  .brand-name {
    font-family: "Ubuntu", sans-serif; font-size: 22px; font-weight: 400; color: #fff;
  }
  .request {
    position: absolute; left: 21px; top: 144px;
    display: flex; gap: 22px;
  }
  .avatar {
    width: 132px; height: 132px; border-radius: 50%;
    background: radial-gradient(circle at 55% 40%, var(--avatar-a), var(--avatar-b));
  }
  .request-text { padding-top: 14px; font-size: 25px; line-height: 29px; letter-spacing: 0.5px; }
  .request-text .sender { color: var(--brand-green); }
  .request-time {
    display: flex; align-items: center; gap: 5px;
    font-family: "Arimo", sans-serif; font-size: 13px; color: var(--muted); margin-top: 8px;
  }
  .section-label {
    position: absolute; left: 32px; top: 318px;
    font-family: "Ubuntu", sans-serif; font-size: 25px; font-weight: 400; letter-spacing: 1px;
  }
  .topic-card {
    position: absolute; left: 30px; width: 611px;
    border: 0; background: var(--card); box-shadow: 0 2px 3px var(--card-shadow);
    display: flex; align-items: center; justify-content: center; text-align: center;
    font-family: "Ubuntu", sans-serif; font-weight: 400;
    font-size: 31px; line-height: 38px; letter-spacing: 1.5px; color: var(--ink);
    padding: 0 14px;
  }
  .topic-card.taste  { top: 388px; height: 142px; }
  .topic-card.travel { top: 583px; height: 142px; }
  .topic-card.weeks  { top: 777px; height: 184px; }
</style>
</head>
<body>
<main class="app-screen">
  <div class="status-bar">
    <svg width="72" height="14" viewBox="0 0 72 14" aria-hidden="true">
      <g fill="#fff"><circle cx="7" cy="7" r="6"/><circle cx="21" cy="7" r="6"/><circle cx="35" cy="7" r="6"/><circle cx="49" cy="7" r="6"/><circle cx="63" cy="7" r="6"/></g>
    </svg>
    <span class="clock">10:30 PM</span>
    <div class="status-right">
      <svg width="28" height="24" viewBox="0 0 28 24" aria-hidden="true">
        <g fill="none" stroke="#fff" stroke-width="3" stroke-linecap="round">
          <path d="M3 9a16 16 0 0 1 22 0"/><path d="M7.5 13.5a10 10 0 0 1 13 0"/>
        </g><circle cx="14" cy="19" r="2.6" fill="#fff"/>
      </svg>
      <span>100%</span>
      <svg width="54" height="24" viewBox="0 0 54 24" aria-hidden="true">
        <rect x="1.5" y="2.5" width="47" height="19" rx="3" fill="none" stroke="#fff" stroke-width="2"/>
        <rect x="4" y="5" width="42" height="14" rx="1.5" fill="#fff"/>
        <rect x="50" y="8" width="3" height="8" rx="1" fill="#fff"/>
      </svg>
    </div>
  </div>

  <header class="app-bar">
    <svg width="36" height="30" viewBox="0 0 36 30" aria-label="Back">
      <g fill="none" stroke="#fff" stroke-width="3" stroke-linecap="round" stroke-linejoin="round">
        <path d="M32 15H4"/><path d="M14 5L4 15l10 10"/>
      </g>
    </svg>
    <h1 class="title">Tell a Story</h1>
    <div class="app-bar-actions">
      <svg width="30" height="32" viewBox="0 0 30 32" aria-label="Notifications">
        <path d="M13 5a8 8 0 0 0-8 8v7l-3 4h22l-3-4v-7a8 8 0 0 0-8-8z" fill="#fff"/>
        <circle cx="13" cy="27" r="3" fill="#fff"/>
        <circle cx="23" cy="6" r="6" fill="var(--alert)"/>
        <text x="23" y="9.5" font-size="9" font-family="Arimo, sans-serif" fill="#fff" text-anchor="middle">2</text>
      </svg>
      <span class="brand-name">Taleway</span>
    </div>
  </header>

  <section class="request">
    <div class="avatar" role="img" aria-label="Profile photo of Marcus"></div>
    <div class="request-text">
      <p><span class="sender">Marcus</span> Want to hear<br>a story!</p>
      <p class="request-time">
        <svg width="12" height="12" viewBox="0 0 12 12" aria-hidden="true">
          <circle cx="6" cy="6" r="5" fill="none" stroke="#c4c4c4" stroke-width="1.2"/>
          <path d="M6 3v3l2 1.5" fill="none" stroke="#c4c4c4" stroke-width="1.2"/>
        </svg>
        11:12 PM
      </p>
    </div>
  </section>

  <h2 class="section-label">Pick a Topic</h2>

  <button class="topic-card taste">What is a taste that you will never<br>enjoy?</button>
  <button class="topic-card travel">Would you rather travel by plane,<br>train or car?</button>
  <button class="topic-card weeks">If you knew you only had two weeks live starting today, What would you spend them doing?</button>
</main>
</body>
</html>
```